Minimalist, Flat(Matte) design for a Beef Jerky packaging company. No bullshit company looking for a

Need a packaging design for a new Beef Jerky product(in English). The name of the company is 'Vellorn' and thus the packaging should reflect the bullish, tough, and simple nature of the beef jerky product. The finished product should communicate simplicity, minimalism, yet toughness and strength.

The logo should be simple, with a minimal number of colors , and should be either all white/cream, or have some red as well. Main colors should be white, cream, tinted red, and matte black. I think 4 colors max would be best. The closest example to an existing package style would be Kessip Noir clove cigarettes( image attached).

It will be on a matte black standing pouch package. See image for package type. Package dimensions:

Dimension: Width x Gusset x Height
INCH : 5.125" (W) x 3.125" (G) x 8.125" (H)
MILLIMETER : 130mm (W) x 80mm (G) x 205mm (H)

I don't have anything totally specific so artistic liberty is encouraged, provided the colors are kept to a minimum and looks consistent with the simple nature of the brand and the matte black packaging.

Also attached an existing beef jerky package with a similar style to what we're looking for.

Industry/Entity Type

It Company

Colors
f59195
ffffff

Requirements
Must have
• Low contrast, flat and minimalist design.
Should not have
• A complicated design with many colors. Gawdy/flashy design. Bright colors. High contrast.

```html
<!DOCTYPE html>
<html lang="en">
<head>
<meta charset="utf-8">
<title>Vellorn Hand Crafted Beef Jerky – Peppered</title>
<link rel="stylesheet" href="https://fonts.googleapis.com/css2?family=Fjalla+One&family=Oswald:wght@500&display=swap">
<style>
  :root {
    --backdrop: #e4e4e4;
    --matte-black: #1c1b19;
    --seal-line: #34332f;
    --tinted-red: #c13b3f;
    --cream: #fbe0b0;
    --cream-line: #d9c59c;
  }
  * { margin: 0; padding: 0; box-sizing: border-box; }
  html, body {
    width: 1200px;
    height: 1111px;
    overflow: hidden;
    background: var(--backdrop);
  }
  .pouch-front {
    position: absolute;
    left: 273px;
    top: 40px;
    width: 654px;
    height: 1031px;
    background: var(--matte-black);
    color: var(--tinted-red);
    font-family: "Fjalla One", "Oswald", sans-serif;
    text-align: center;
  }
  .pouch-lines {
    position: absolute;
    inset: 0;
  }
  .headline {
    position: absolute;
    left: 0;
    right: 0;
    text-transform: uppercase;
    line-height: 1;
  }
  .headline--craft { top: 212px; font-size: 60px; letter-spacing: 1px; }
  .headline--product { top: 296px; font-size: 82px; letter-spacing: 2px; }
  .brand-name {
    position: absolute;
    left: 0;
    right: 0;
    top: 480px;
    font-size: 112px;
    line-height: 1;
    letter-spacing: 3px;
    color: var(--tinted-red);
  }
  .flavour {
    position: absolute;
    left: 0;
    right: 0;
    top: 690px;
    font-size: 44px;
    line-height: 1;
    letter-spacing: 1px;
  }
  .tool-mark {
    position: absolute;
    left: 279px;
    top: 792px;
    width: 96px;
    height: 96px;
    border: 2px solid var(--cream-line);
    background: var(--matte-black);
    padding: 14px;
  }
  .tool-mark__art {
    width: 100%;
    height: 100%;
    background: linear-gradient(135deg, #4a2a28, #3a2220);
  }
  .net-weight {
    position: absolute;
    left: 0;
    right: 0;
    top: 900px;
    font-family: "Oswald", sans-serif;
    font-weight: 500;
    font-size: 16px;
    color: var(--cream);
    letter-spacing: 0.5px;
  }
</style>
</head>
<body>
  <main class="pouch-front">
    <svg class="pouch-lines" width="654" height="1031" viewBox="0 0 654 1031" aria-hidden="true">
      <line x1="0" y1="36" x2="654" y2="36" stroke="var(--seal-line)" stroke-width="2"/>
      <line x1="14" y1="66" x2="640" y2="66" stroke="var(--seal-line)" stroke-width="2" stroke-dasharray="6 6"/>
      <line x1="0" y1="88" x2="654" y2="88" stroke="var(--seal-line)" stroke-width="2"/>
      <line x1="0" y1="283" x2="654" y2="283" stroke="var(--cream-line)" stroke-width="2"/>
      <path d="M0 733 Q 327 930 654 733" fill="none" stroke="var(--cream-line)" stroke-width="2"/>
    </svg>

    <h1 class="headline headline--craft">Hand Crafted</h1>
    <h2 class="headline headline--product">Beef Jerky</h2>

    <p class="brand-name">VELLORN</p>

    <p class="flavour">PEPPERED</p>

    <div class="tool-mark">
      <div class="tool-mark__art" role="img" aria-label="Crossed butcher cleaver and knife emblem"></div>
    </div>

    <p class="net-weight">NET WT. 3oz/100g</p>
  </main>
</body>
</html>
```